High-end residential home builder needs a business card design

We need a new business card design for a small residential construction company based in Boise, Idaho. We specialize in building custom high-end homes and remodels, with a focus on great design and craftsmanship.

We would like to use our current logo, but open to new color suggestions.
Just looking for a clean, sharp, modern design that looks high-end.

Target Market(s)

Upscale clientele

Industry/Entity Type

Contractor

Contact Information for Business Card

Company: Stonefield Custom Builders
Name: Marcus Tilley
Phone number: 208 367 4120
Email: MarcusTilleySCB@mailbox-example.com
Website: Stonefieldcustombuilders-example.com

Font styles to use
Serif
Sans Serif

Requirements
Must have
• Company Logo
Company name
My name
My phone number
My email
Company website
Nice to have
• I have attached a few photos of cards that I really like.

```html
<!DOCTYPE html>
<html lang="en">
<head>
<meta charset="utf-8">
<title>Stonefield Custom Builders — Business Card</title>
<link rel="stylesheet" href="https://fonts.googleapis.com/css2?family=Montserrat:wght@400;500&family=Open+Sans:wght@400&display=swap">
<style>
  :root {
    --backdrop: #2d2e2c;
    --card-dark: #121212;
    --card-light: #ffffff;
    --copper: #c98a4b;
    --copper-light: #e8a45f;
    --ink: #3b3a39;
    --muted: #7c7f86;
  }
  * { box-sizing: border-box; margin: 0; padding: 0; }
  html, body {
    width: 1200px; height: 824px; overflow: hidden;
    background: var(--backdrop);
  }
  .canvas {
    position: relative; width: 1200px; height: 824px;
    display: flex; align-items: center; justify-content: center; gap: 60px;
  }
  .card {
    position: relative; width: 500px; height: 286px;
    box-shadow: 0 10px 30px rgba(0,0,0,.45);
  }

  /* Front */
  .card--front {
    background: var(--card-dark);
    display: flex; align-items: center; justify-content: center; gap: 22px;
  }
  .brand-mark {
    width: 58px; height: 58px;
    border: 2px solid var(--copper);
  }
  .brand-name {
    font-family: "Montserrat", sans-serif; font-weight: 400;
    color: var(--copper);
    text-transform: uppercase; letter-spacing: 4px;
    font-size: 22px; line-height: 1.35;
  }
  .brand-name span { display: block; font-size: 14px; letter-spacing: 3.6px; }

  /* Back */
  .card--back {
    background: var(--card-light);
    display: flex; align-items: center;
    padding: 0 34px 0 42px; gap: 34px;
  }
  .back-brand {
    display: flex; flex-direction: column; align-items: center; gap: 10px;
    width: 108px;
  }
  .back-brand .brand-mark { width: 66px; height: 66px; border-color: var(--ink); }
  .back-brand .brand-name {
    color: var(--ink); font-size: 10px; letter-spacing: 1.6px; text-align: center;
  }
  .contact { display: flex; flex-direction: column; }
  .person-name {
    font-family: "Montserrat", sans-serif; font-weight: 500;
    font-size: 23px; letter-spacing: 1.2px; color: var(--ink);
    text-transform: uppercase; margin-bottom: 14px;
  }
  .contact-line {
    display: flex; align-items: center; gap: 8px;
    font-family: "Open Sans", sans-serif; font-size: 11.5px;
    color: var(--muted); line-height: 1.9;
  }
  .contact-line svg { width: 11px; height: 11px; flex: none; }
  .icon { fill: var(--copper-light); stroke: none; }
  .icon-stroke { fill: none; stroke: var(--copper-light); stroke-width: 1.6; }
</style>
</head>
<body>
<main class="canvas">
  <section class="card card--front">
    <div class="brand-mark"></div>
    <p class="brand-name">Stonefield<span>Custom Builders</span></p>
  </section>

  <section class="card card--back">
    <div class="back-brand">
      <div class="brand-mark"></div>
      <p class="brand-name">Stonefield Custom Builders</p>
    </div>
    <div class="contact">
      <h1 class="person-name">Marcus Tilley</h1>
      <p class="contact-line">
        <svg viewBox="0 0 12 12" aria-hidden="true"><path class="icon" d="M2.4 1h2l1 2.6-1.3 1a6 6 0 0 0 3.3 3.3l1-1.3L11 7.6v2A1.4 1.4 0 0 1 9.6 11 8.6 8.6 0 0 1 1 2.4 1.4 1.4 0 0 1 2.4 1z"/></svg>
        208 367 4120
      </p>
      <p class="contact-line">
        <svg viewBox="0 0 12 12" aria-hidden="true"><path class="icon" d="M0 2.5h12v7H0z"/><path d="M0.5 3l5.5 4 5.5-4" fill="none" stroke="#fff" stroke-width="1"/></svg>
        MarcusTilleySCB@mailbox-example.com
      </p>
      <p class="contact-line">
        <svg viewBox="0 0 12 12" aria-hidden="true"><circle class="icon-stroke" cx="6" cy="6" r="5"/><path class="icon-stroke" d="M1 6h10M6 1c-2.6 3-2.6 7 0 10M6 1c2.6 3 2.6 7 0 10"/></svg>
        Stonefieldcustombuilders-example.com
      </p>
    </div>
  </section>
</main>
</body>
</html>
```